Business Card Design Project

1. Show the company logo.
2. Only company email ID and website address to be shown (office@zolotoyveter.fm , www.zolotoyveter.fm).
3. Logo to be provided by us, 2 designs just in case. The logo is made with ' Zolotoy Veter' text, need to be edited so that it shows 'Tikhaya Gavan' instead .
4. Single sided business card, portrait or landscape is not a problem; back side to be filled with colors or a design that matches the logo the best.
5. Logo is to be embossed.
6. We're looking at an English and Russian version.
7. any other better idea is always welcomed.

```html
<!DOCTYPE html>
<html lang="en">
<head>
<meta charset="utf-8">
<title>Tikhaya Gavan — Business Card</title>
<link rel="stylesheet" href="https://fonts.googleapis.com/css2?family=Mulish:wght@400;700&display=swap">
<style>
  :root {
    --page: #2b2b2d;
    --card-blue-light: #5a93cf;
    --card-blue: #3f78b8;
    --card-blue-deep: #2e66a8;
    --navy: #24457f;
    --navy-deep: #1d3a6e;
    --gold: #fbbf1a;
    --white: #ffffff;
  }
  * { box-sizing: border-box; margin: 0; padding: 0; }
  html, body {
    width: 1200px;
    height: 900px;
    overflow: hidden;
    background: var(--page);
    font-family: "Mulish", sans-serif;
  }
  .stage {
    position: relative;
    width: 1200px;
    height: 900px;
    display: flex;
    justify-content: center;
    align-items: center;
    gap: 80px;
  }
  .card {
    position: relative;
    width: 380px;
    height: 660px;
    border-radius: 4px;
    overflow: hidden;
    box-shadow: 0 18px 40px rgba(0, 0, 0, 0.45);
  }
  .card--front {
    background: radial-gradient(circle at 55% 40%, var(--card-blue-light) 0%, var(--card-blue) 45%, var(--card-blue-deep) 100%);
  }
  .card--back {
    background: linear-gradient(160deg, var(--navy) 0%, var(--navy-deep) 100%);
    display: flex;
    justify-content: center;
    align-items: center;
  }
  .brand {
    position: absolute;
    top: 70px;
    left: 50%;
    transform: translateX(-50%);
    width: 260px;
    height: 260px;
    border-radius: 50%;
    background: var(--navy);
    display: flex;
    justify-content: center;
    align-items: center;
  }
  .brand__name {
    color: var(--white);
    font-weight: 700;
    font-size: 26px;
    letter-spacing: 2px;
    text-transform: uppercase;
    text-align: center;
    line-height: 1.25;
  }
  .contacts {
    position: absolute;
    top: 430px;
    left: 0;
    right: 0;
    text-align: center;
  }
  .contact + .contact { margin-top: 26px; }
  .contact__label {
    display: block;
    color: var(--gold);
    font-weight: 700;
    font-size: 19px;
    line-height: 1.2;
  }
  .contact__value {
    display: block;
    color: var(--white);
    font-weight: 400;
    font-size: 23px;
    line-height: 1.3;
  }
  .back-name {
    color: var(--gold);
    font-weight: 700;
    font-size: 40px;
    letter-spacing: 3px;
    text-transform: uppercase;
    text-align: center;
    line-height: 1.2;
  }
</style>
</head>
<body>
  <main class="stage">
    <section class="card card--front" aria-label="Business card, front">
      <div class="brand">
        <p class="brand__name">Tikhaya<br>Gavan</p>
      </div>
      <div class="contacts">
        <p class="contact">
          <span class="contact__label">email</span>
          <span class="contact__value">office@zolotoyveter.fm</span>
        </p>
        <p class="contact">
          <span class="contact__label">web</span>
          <span class="contact__value">www.zolotoyveter.fm</span>
        </p>
      </div>
    </section>
    <section class="card card--back" aria-label="Business card, back">
      <p class="back-name">Tikhaya<br>Gavan</p>
    </section>
  </main>
</body>
</html>
```